New design of skin care labels for a natural makeup company

Our company sells 100% natural makeup and also offers a small selection of skin care cosmetics which aren't fully organic but have natural ingredients where possible and made by hand in small batches.
We are an English company with Japanese influence in that our staff and company name are Japanese, we understand how natural cosmetics in Japan are a huge business as demanded by Japanese girls and we include some Japanese ingredients in our cosmetics though we are marketing and selling in the UK.
We want to re-design the labels for 6 lines of our skin care range of cosmetics. These would be a mix of toners, creams, gels & face wash. There are 3 label sizes HxW:
50 x 120 mm
65 x 130 mm
90 x 115 mm
Our products are priced between £10-£15 so not expensive but not drug store budget prices either. We want the new labels to portray:
More luxury than common every day counter products
More natural than chemically preserved, fragranced, artificial products
Show they are free from parabens/sulphates and possibly even announce hand made in England
They need to include the usual necessary information like ingredients, usage instructions, warnings, weights, contact details along with our logo which is trademarked so unfortunately can't be altered or recoloured as its a mono logo.
We are open to all your ideas but our instincts will probably favour something clean/clear looking rather than fussy - though not too minimalist. Our bottles are either clear or semi transparent so we might prefer a see-thru label to show off the product. However these are just ideas at the moment and we may decide against them after seeing your various designs.
Females who care more about what they put on their skin.
Cosmetics

```html
<!DOCTYPE html>
<html lang="en">
<head>
<meta charset="utf-8">
<title>Mizuka Natural Face Care – Label Set</title>
<link rel="stylesheet" href="https://fonts.googleapis.com/css2?family=Questrial&family=Arimo:wght@400;700&display=swap">
<style>
  :root {
    --canvas-bg: #f4f4f4;
    --label-bg: #ffffff;
    --label-edge: #dcdcdc;
    --ink: #2b2b2b;
    --ink-soft: #555555;
    --brand-block: #1c1a1a;
    --brand-text: #ffffff;
    --rule: #3a3a3a;
    --accent: #d3175a;
    --accent-text: #ffffff;
  }
  html, body {
    margin: 0;
    padding: 0;
    width: 1200px;
    height: 1000px;
    overflow: hidden;
    background: var(--canvas-bg);
  }
  .canvas {
    position: relative;
    width: 1200px;
    height: 1000px;
  }
  .label {
    position: absolute;
    background: var(--label-bg);
    border: 1px solid var(--label-edge);
    box-sizing: border-box;
  }
  .brand-block {
    position: absolute;
    background: var(--brand-block);
    display: flex;
    flex-direction: column;
    align-items: center;
    justify-content: center;
    gap: 12px;
  }
  .brand-mark {
    display: block;
  }
  .brand-name {
    font-family: "Arimo", Arial, sans-serif;
    font-weight: 700;
    color: var(--brand-text);
    letter-spacing: 0.08em;
  }
  .range-name {
    position: absolute;
    font-family: "Questrial", "Century Gothic", sans-serif;
    color: var(--ink-soft);
    line-height: 1.15;
    text-transform: uppercase;
  }
  .rule {
    position: absolute;
    height: 2px;
    background: var(--rule);
  }
  .product-name {
    position: absolute;
    font-family: "Arimo", Arial, sans-serif;
    font-weight: 700;
    color: var(--ink);
    line-height: 1.25;
    text-transform: uppercase;
    letter-spacing: 0.02em;
  }
  .product-notes {
    position: absolute;
    font-family: "Questrial", "Century Gothic", sans-serif;
    color: var(--ink-soft);
    line-height: 1.3;
  }
  .volume {
    position: absolute;
    font-family: "Questrial", "Century Gothic", sans-serif;
    color: var(--ink-soft);
  }
  .skin-badge {
    position: absolute;
    background: var(--accent);
    color: var(--accent-text);
    font-family: "Arimo", Arial, sans-serif;
    font-weight: 700;
    text-transform: uppercase;
    letter-spacing: 0.03em;
    display: flex;
    align-items: center;
    justify-content: center;
    white-space: nowrap;
  }

  /* Moisturizer label */
  .label--moisturizer { left: 150px; top: 470px; width: 340px; height: 460px; }
  .label--moisturizer .brand-block { left: 22px; top: 24px; width: 96px; height: 176px; }
  .label--moisturizer .brand-name { font-size: 15px; }
  .label--moisturizer .range-name { left: 142px; top: 92px; font-size: 22px; }
  .label--moisturizer .rule--top { left: 22px; top: 210px; width: 270px; }
  .label--moisturizer .product-name { left: 26px; top: 222px; font-size: 19px; }
  .label--moisturizer .rule--bottom { left: 22px; top: 286px; width: 270px; }
  .label--moisturizer .product-notes { left: 26px; top: 300px; font-size: 17px; }
  .label--moisturizer .volume { left: 26px; top: 410px; font-size: 15px; }
  .label--moisturizer .skin-badge { left: 170px; top: 400px; width: 152px; height: 30px; font-size: 12px; }

  /* Facial wash label */
  .label--wash { left: 520px; top: 580px; width: 260px; height: 350px; }
  .label--wash .brand-block { left: 20px; top: 22px; width: 78px; height: 140px; }
  .label--wash .brand-name { font-size: 12px; }
  .label--wash .range-name { left: 116px; top: 78px; font-size: 19px; }
  .label--wash .rule--top { left: 20px; top: 170px; width: 220px; }
  .label--wash .product-name { left: 22px; top: 182px; font-size: 16px; }
  .label--wash .rule--bottom { left: 20px; top: 236px; width: 220px; }
  .label--wash .product-notes { left: 22px; top: 248px; font-size: 14px; }
  .label--wash .volume { left: 22px; top: 322px; font-size: 13px; }
  .label--wash .skin-badge { left: 118px; top: 314px; width: 126px; height: 26px; font-size: 10.5px; }

  /* Toner label */
  .label--toner { left: 810px; top: 290px; width: 240px; height: 640px; }
  .label--toner .brand-block { left: 18px; top: 20px; width: 86px; height: 260px; }
  .label--toner .brand-name { font-size: 13px; }
  .label--toner .range-name { left: 120px; top: 200px; font-size: 18px; }
  .label--toner .rule--top { left: 18px; top: 288px; width: 204px; }
  .label--toner .product-name { left: 20px; top: 300px; font-size: 16px; }
  .label--toner .rule--bottom { left: 18px; top: 354px; width: 204px; }
  .label--toner .product-notes { left: 20px; top: 368px; width: 204px; font-size: 13px; }
  .label--toner .volume { left: 20px; top: 490px; font-size: 15px; }
  .label--toner .skin-badge { left: 18px; top: 556px; width: 160px; height: 30px; font-size: 12px; }
</style>
</head>
<body>
<main class="canvas">

  <section class="label label--moisturizer" aria-label="Natural Face Moisturizer label">
    <div class="brand-block">
      <svg class="brand-mark" width="34" height="34" viewBox="0 0 34 34" aria-hidden="true">
        <circle cx="17" cy="17" r="15" fill="none" stroke="#ffffff" stroke-width="2"/>
      </svg>
      <span class="brand-name">MIZUKA</span>
    </div>
    <p class="range-name" style="margin:0">Natural<br>Face<br>Care</p>
    <div class="rule rule--top"></div>
    <h2 class="product-name" style="margin:0">Natural Face<br>Moisturizer</h2>
    <div class="rule rule--bottom"></div>
    <p class="product-notes" style="margin:0">Anti-Oxidant<br>Fragrance, SLS &amp; Etc.</p>
    <span class="volume">150 mL</span>
    <span class="skin-badge">For all skin type</span>
  </section>

  <section class="label label--wash" aria-label="Seaweed and Lime Facial Wash label">
    <div class="brand-block">
      <svg class="brand-mark" width="28" height="28" viewBox="0 0 28 28" aria-hidden="true">
        <circle cx="14" cy="14" r="12" fill="none" stroke="#ffffff" stroke-width="2"/>
      </svg>
      <span class="brand-name">MIZUKA</span>
    </div>
    <p class="range-name" style="margin:0">Natural<br>Face<br>Care</p>
    <div class="rule rule--top"></div>
    <h2 class="product-name" style="margin:0">Seaweed &amp; Lime<br>Facial Wash</h2>
    <div class="rule rule--bottom"></div>
    <p class="product-notes" style="margin:0">Anti-Oxidant<br>SLS lorem ipsum, lorem</p>
    <span class="volume">150 mL</span>
    <span class="skin-badge">For all skin type</span>
  </section>

  <section class="label label--toner" aria-label="Marine Collagen Hydrating Toner label">
    <div class="brand-block">
      <svg class="brand-mark" width="30" height="30" viewBox="0 0 30 30" aria-hidden="true">
        <circle cx="15" cy="15" r="13" fill="none" stroke="#ffffff" stroke-width="2"/>
      </svg>
      <span class="brand-name">MIZUKA</span>
    </div>
    <p class="range-name" style="margin:0">Natural<br>Face<br>Care</p>
    <div class="rule rule--top"></div>
    <h2 class="product-name" style="margin:0">Marine Collagen<br>Hydrating Toner</h2>
    <div class="rule rule--bottom"></div>
    <p class="product-notes" style="margin:0">Hydrate, purify and help to reduce the effects of aging with Mizuka Marine Collagen Hydrating Toner.</p>
    <span class="volume">150 mL</span>
    <span class="skin-badge">For all skin type</span>
  </section>

</main>
</body>
</html>
```